We have a new App which runs on the Android platform We need an icon for the App and design / logo / branding for a single web page. We are able to build the web page but need help with the logo/icon for the App and the web page. We have chosen the brand name Pexalunar. The App allows the user to enter one language and it will translate to another language plus speak it in the selected language. The Android App needs the Icon plus the splash screen & background screen. Thanks

```html
<!DOCTYPE html>
<html lang="en">
<head>
<meta charset="utf-8">
<title>Pexalunar – Language Translator</title>
<link rel="stylesheet" href="https://fonts.googleapis.com/css2?family=Open+Sans:wght@700&family=Arimo:wght@400&family=Patrick+Hand&display=swap">
<style>
  :root {
    --bg-top: #eaf1fa;
    --bg-bottom: #f7fafd;
    --brand-blue: #129fe3;
    --bar-blue: #31b8ee;
    --bar-blue-dark: #1a9fdc;
    --field-blue: #46c4f2;
    --tag-grey: #8a8a8a;
    --text-dark: #2b2b2b;
    --box-fill: #ededed;
    --box-line: #d2d2d2;
    --screen-white: #ffffff;
    --icon-white: #ffffff;
  }
  * { box-sizing: border-box; margin: 0; padding: 0; }
  html, body { width: 1200px; height: 675px; overflow: hidden; }
  body {
    position: relative;
    background: linear-gradient(180deg, var(--bg-top) 0%, var(--bg-bottom) 60%);
    font-family: "Arimo", Arial, sans-serif;
  }

  /* Shared brand lock-up */
  .brand { display: flex; align-items: center; justify-content: center; gap: 12px; }
  .brand__dot { border-radius: 50%; background: var(--brand-blue); flex: none; }
  .brand__name {
    font-family: "Open Sans", sans-serif;
    font-weight: 700;
    color: var(--brand-blue);
    letter-spacing: -0.5px;
    line-height: 1;
  }
  .brand__tagline {
    font-family: "Patrick Hand", cursive;
    color: var(--tag-grey);
    text-align: center;
  }

  /* Splash screen */
  .splash {
    position: absolute; left: 80px; top: 140px; width: 242px; height: 405px;
    background: linear-gradient(180deg, #ffffff 0%, #f2f7fc 100%);
    border: 1px solid #dfe6ee;
    display: flex; flex-direction: column; align-items: center; justify-content: center;
    padding-top: 90px;
  }
  .splash .brand__dot { width: 16px; height: 16px; }
  .splash .brand { gap: 6px; }
  .splash .brand__name { font-size: 24px; }
  .splash .brand__tagline { font-size: 11px; margin-top: 2px; }

  /* Central wordmark */
  .wordmark {
    position: absolute; left: 400px; top: 360px; width: 400px;
    display: flex; flex-direction: column; align-items: center;
  }
  .wordmark .brand__dot { width: 40px; height: 40px; }
  .wordmark .brand__name { font-size: 60px; }
  .wordmark .brand__tagline { font-size: 31px; margin-top: 4px; letter-spacing: 0.5px; }

  /* Translator screen */
  .translator {
    position: absolute; left: 882px; top: 140px; width: 260px; height: 396px;
    background: var(--screen-white);
    border: 1px solid #dfe6ee;
    display: flex; flex-direction: column;
  }
  .translator__bar {
    height: 28px; background: var(--bar-blue);
    display: flex; align-items: center; justify-content: space-between; padding: 0 8px;
  }
  .translator__body { flex: 1; padding: 8px 18px 0; display: flex; flex-direction: column; }
  .text-box {
    background: var(--box-fill); border: 1px solid var(--box-line);
    font-size: 7.6px; line-height: 14px; color: var(--text-dark);
    padding: 5px 6px;
  }
  .controls { display: flex; justify-content: space-between; padding: 8px 36px 0; }
  .round-btn {
    width: 28px; height: 28px; border-radius: 50%;
    background: linear-gradient(180deg, #45ccf6 0%, #0f95da 100%);
    display: flex; align-items: center; justify-content: center;
  }
  .lang-select {
    margin: 8px 12px 6px; height: 27px; background: var(--field-blue);
    display: flex; align-items: center; justify-content: space-between;
    color: var(--icon-white); font-size: 10px; padding-left: 8px;
  }
  .lang-select__arrow {
    width: 26px; height: 100%; background: var(--bar-blue-dark);
    display: flex; align-items: center; justify-content: center;
  }
  .copy-btn {
    align-self: center; margin-top: 2px; width: 104px; height: 30px;
    background: linear-gradient(180deg, #3fc6f5 0%, #13a3e5 100%);
    color: var(--icon-white); font-size: 9.5px;
    display: flex; align-items: center; justify-content: center;
  }
  .translator__foot { height: 12px; background: var(--bar-blue); margin-top: 12px; }
</style>
</head>
<body>

  <section class="splash" aria-label="Splash screen">
    <div class="brand">
      <span class="brand__dot"></span>
      <span class="brand__name">Pexalunar</span>
    </div>
    <p class="brand__tagline">language Translator</p>
  </section>

  <section class="wordmark" aria-label="Brand wordmark">
    <div class="brand">
      <span class="brand__dot"></span>
      <span class="brand__name">Pexalunar</span>
    </div>
    <p class="brand__tagline">language Translator</p>
  </section>

  <section class="translator" aria-label="Translator screen">
    <header class="translator__bar">
      <svg width="14" height="12" viewBox="0 0 14 12" aria-label="Back">
        <path d="M1 6 L13 1 L9 6 L13 11 Z" fill="#1b7fbf"/>
      </svg>
      <svg width="16" height="12" viewBox="0 0 16 12" aria-label="Menu">
        <rect y="1" width="16" height="1.6" fill="#1b7fbf"/>
        <rect y="5.2" width="16" height="1.6" fill="#1b7fbf"/>
        <rect y="9.4" width="16" height="1.6" fill="#1b7fbf"/>
      </svg>
    </header>

    <div class="translator__body">
      <p class="text-box">Type or paste the sentence you want to hear in another language here. The app reads your words, finds the closest meaning and prepares a clear version for the language you pick below. Tap the microphone to speak instead of typing, or tap the arrows to swap the two languages around.</p>

      <div class="controls">
        <span class="round-btn" aria-label="Speak">
          <svg width="12" height="14" viewBox="0 0 12 14">
            <rect x="3.5" y="0.5" width="5" height="8" rx="2.5" fill="#fff"/>
            <path d="M1.5 6.5 a4.5 4.5 0 0 0 9 0" fill="none" stroke="#fff" stroke-width="1.3"/>
            <rect x="5.4" y="11" width="1.2" height="2.5" fill="#fff"/>
          </svg>
        </span>
        <span class="round-btn" aria-label="Swap languages">
          <svg width="14" height="14" viewBox="0 0 14 14" fill="none" stroke="#fff" stroke-width="1.6">
            <path d="M2.5 6 A4.7 4.7 0 0 1 11 4"/>
            <path d="M11.5 8 A4.7 4.7 0 0 1 3 10"/>
            <path d="M11.6 1.2 L11.2 4.4 L8 4" stroke-linejoin="round"/>
            <path d="M2.4 12.8 L2.8 9.6 L6 10" stroke-linejoin="round"/>
          </svg>
        </span>
      </div>

      <div class="lang-select">
        <span>French</span>
        <span class="lang-select__arrow">
          <svg width="9" height="6" viewBox="0 0 9 6"><path d="M0 0 H9 L4.5 6 Z" fill="#8fdcf7"/></svg>
        </span>
      </div>

      <p class="text-box">Saisissez ou collez la phrase que vous voulez entendre dans une autre langue. L'application lit vos mots, trouve le sens le plus proche et prépare une version claire. Touchez le micro pour parler au lieu d'écrire. Le texte traduit apparaît ici.</p>

      <span class="copy-btn">Copy Clipboard</span>
    </div>

    <footer class="translator__foot"></footer>
  </section>

</body>
</html>
```